Kestra Health- Welcome

Under New Management / New Staff & New Physicians

Offering More Services

Accepting New Patients

Two Locations in the Bronx: North Bronx: 2915 Pellam Road – Office Phone: 718-555-0143
South Bronx: 564 Corvin Street – Office Phone: 718-555-0187

Our Services:
Primary Care
Gynecology
Cardiology
Dentistry
Psychology
Psychiatry
Neurology
Pain Management
Gastroenterology
Podiatry
Dermatology
Vascular Surgery
Physical Therapy
HIV / Infectious Disease

For an ZRPQ Mailing - we will drop off to Post Office

Front English
Back Smaller to have post office specs but have it in Spanish

```html
<!DOCTYPE html>
<html lang="en">
<head>
<meta charset="utf-8">
<title>Kestra Health Postcard – Front and Back</title>
<link rel="stylesheet" href="https://fonts.googleapis.com/css2?family=Montserrat:ital,wght@0,400;0,500;0,600;0,700;1,700;1,800&display=swap">
<style>
  :root {
    --navy: #1e3180;
    --red: #b8192f;
    --board: #dcdcdc;
    --beige: #eeebe1;
    --white: #ffffff;
    --ink: #2b2b2b;
    --photo-green: #6f7d48;
    --photo-warm: #b59a74;
  }
  * { box-sizing: border-box; margin: 0; padding: 0; }
  html, body { width: 923px; height: 1200px; overflow: hidden; }
  body {
    background: var(--board);
    font-family: "Montserrat", Arial, sans-serif;
    color: var(--ink);
    position: relative;
  }
  .postcard {
    position: absolute;
    left: 92px;
    width: 738px;
    height: 508px;
    background: var(--white);
    box-shadow: 4px 6px 8px rgba(0,0,0,0.28);
    overflow: hidden;
  }
  .postcard--front { top: 58px; }
  .postcard--back { top: 596px; }
  .abs { position: absolute; }

  /* Front */
  .hero {
    left: 0; top: 0; width: 738px; height: 386px;
    background: linear-gradient(90deg, var(--photo-green) 0%, #8a7a5c 28%, var(--photo-warm) 45%, #d8d0bd 58%, var(--beige) 68%);
  }
  .front-copy { left: 385px; width: 320px; text-align: center; white-space: nowrap; }
  .headline {
    top: 58px;
    font-weight: 800; font-style: italic;
    font-size: 27px; line-height: 34px;
    color: var(--navy);
  }
  .headline .accent { color: var(--red); }
  .intro {
    top: 145px;
    font-size: 17px; line-height: 27px; font-weight: 500;
    color: var(--navy);
  }
  .offer {
    top: 203px;
    font-size: 16px; line-height: 26px; font-weight: 600;
    color: var(--red);
  }
  .thumb {
    top: 274px; width: 94px; height: 61px;
    border: 1px solid var(--navy);
    outline: 2px solid var(--white); outline-offset: -3px;
  }
  .thumb--scan { left: 398px; background: linear-gradient(135deg, #c9c4c0, #e6d0c0 60%, #8f9aa6); }
  .thumb--exam { left: 501px; background: linear-gradient(135deg, #e9edf1, #c9ad96 55%, #f2f2f2); }
  .thumb--meter { left: 604px; background: linear-gradient(135deg, #f3f3f3, #e2c7b2 50%, #d9dde2); }

  .card-line { left: 0; top: 0; width: 738px; height: 508px; pointer-events: none; }

  .location { font-size: 13.5px; line-height: 17px; color: var(--ink); white-space: nowrap; }
  .location h3 { font-size: 13.5px; font-weight: 700; color: var(--red); }
  .location--north { left: 27px; }
  .location--south { left: 248px; }
  .divider { left: 230px; width: 1px; height: 48px; background: #c9c9c9; }

  .brand { display: flex; align-items: center; gap: 8px; }
  .brand-square { width: 14px; height: 14px; background: var(--navy); }
  .brand-name { font-size: 30px; font-weight: 700; color: var(--navy); letter-spacing: 0.5px; white-space: nowrap; }
  .brand-tagline { font-size: 8.5px; font-weight: 700; font-style: italic; color: var(--navy); text-align: center; white-space: nowrap; }

  .side-label {
    position: absolute; left: 842px;
    font-size: 14px; color: #555;
    transform: rotate(-90deg); transform-origin: left top;
  }

  /* Back */
  .team-photo {
    left: 0; top: 0; width: 402px; height: 336px;
    background: linear-gradient(120deg, #cfd6dc 0%, #eef0f2 35%, #dcdfe3 60%, #f4f5f6 100%);
  }
  .services-panel {
    left: 0; top: 190px; width: 402px; height: 146px;
    background: var(--navy);
  }
  .services-title {
    left: 61px; top: 180px; width: 280px; height: 21px;
    background: var(--red); border-radius: 11px;
    color: var(--white); font-weight: 700; font-size: 16px; line-height: 21px;
    text-align: center; white-space: nowrap;
  }
  .services-list {
    left: 0; top: 220px; width: 402px;
    text-align: center; color: var(--white);
    font-size: 13px; line-height: 19.5px; font-weight: 500;
    white-space: nowrap;
  }
  .services-list .dot { color: var(--red); font-size: 9px; vertical-align: 2px; margin: 0 1px; }
  .slogan {
    left: 0; top: 340px; width: 390px;
    text-align: center; color: var(--white);
    font-weight: 800; font-style: italic; font-size: 15px; line-height: 19px;
    white-space: nowrap;
  }
  .stamp { left: 639px; top: 36px; width: 67px; height: 67px; border: 1px solid #555; }
  .caption {
    position: absolute; top: 1138px; left: 0; width: 923px;
    text-align: center; font-size: 14px; color: #444; letter-spacing: 0.5px;
  }
</style>
</head>
<body>

<section class="postcard postcard--front" aria-label="Postcard front">
  <div class="abs hero" role="img" aria-label="Photo of a smiling woman beside an older man in a wheelchair in a park, fading into a light beige backdrop"></div>

  <h1 class="abs front-copy headline">Better Care<br><span class="accent">for a Better</span> Life</h1>
  <p class="abs front-copy intro">Under New Management<br>New Staff &amp; New Physicians</p>
  <p class="abs front-copy offer">Offering More Services<br>Accepting New Patients</p>

  <div class="abs thumb thumb--scan" role="img" aria-label="Photo of an ultrasound scan on a patient"></div>
  <div class="abs thumb thumb--exam" role="img" aria-label="Photo of a doctor examining a young man"></div>
  <div class="abs thumb thumb--meter" role="img" aria-label="Photo of a blood glucose test"></div>

  <svg class="abs card-line" viewBox="0 0 738 508" aria-hidden="true">
    <path d="M0 386 H738 V508 H0 Z" fill="var(--white)"/>
    <path d="M0 386 H343 L358 342 L375 425 L386 386 H738" fill="none" stroke="var(--navy)" stroke-width="3"/>
  </svg>

  <div class="abs location location--north" style="top:428px">
    <h3>North Bronx:</h3>
    <p>2915 Pellam Road –</p>
    <p>Office Phone: 718-555-0143</p>
  </div>
  <div class="abs divider" style="top:428px"></div>
  <div class="abs location location--south" style="top:428px">
    <h3>South Bronx:</h3>
    <p>564 Corvin Street – Office</p>
    <p>Phone: 718-555-0187</p>
  </div>

  <div class="abs brand" style="left:494px; top:438px">
    <span class="brand-square"></span>
    <span class="brand-name">Kestra Health</span>
  </div>
</section>
<span class="side-label" style="top:566px">Front</span>

<section class="postcard postcard--back" lang="es" aria-label="Reverso de la postal">
  <div class="abs team-photo" role="img" aria-label="Foto de una paciente con un médico y una enfermera en una clínica luminosa"></div>
  <div class="abs services-panel"></div>
  <div class="abs services-title">Servicios que Ofrecemos</div>
  <div class="abs services-list">
    <p><span class="dot">●</span> Atención Primaria <span class="dot">●</span> Ginecología <span class="dot">●</span> Cardiología</p>
    <p><span class="dot">●</span> Odontología <span class="dot">●</span> Psicología <span class="dot">●</span> Psiquiatría</p>
    <p><span class="dot">●</span> Neurología <span class="dot">●</span> Manejo del Dolor <span class="dot">●</span> Gastroenterología</p>
    <p><span class="dot">●</span> Podiatría <span class="dot">●</span> Dermatología <span class="dot">●</span> Cirugía Vascular</p>
    <p><span class="dot">●</span> Terapia Física <span class="dot">●</span> VIH/Enfermedades Infecciosas</p>
  </div>

  <svg class="abs card-line" viewBox="0 0 738 508" aria-hidden="true">
    <path d="M0 336 H402 L388 386 H0 Z" fill="var(--red)"/>
    <path d="M0 386 H388 L404 342 L419 426 L430 386 H738" fill="none" stroke="var(--navy)" stroke-width="3"/>
  </svg>
  <p class="abs slogan">¡Experimente un nivel de servicio<br>que no encontrará en ningún otro lugar!</p>

  <div class="abs stamp"></div>

  <div class="abs location location--north" style="top:429px">
    <h3>Bronx Norte:</h3>
    <p>2915 Pellam Road – Oficina</p>
    <p>Teléfono: 718-555-0143</p>
  </div>
  <div class="abs divider" style="top:429px"></div>
  <div class="abs location location--south" style="top:429px">
    <h3>Bronx Sur:</h3>
    <p>564 Corvin Street – Oficina</p>
    <p>Teléfono: 718-555-0187</p>
  </div>

  <div class="abs" style="left:510px; top:420px; width:196px">
    <div class="brand">
      <span class="brand-square"></span>
      <span class="brand-name" style="font-size:26px">Kestra Health</span>
    </div>
    <p class="brand-tagline" style="margin-top:8px; border-top:1px solid var(--red); border-bottom:1px solid var(--red); padding:3px 0">Mejor Atención para una Mejor Vida</p>
  </div>
</section>
<span class="side-label" style="top:1104px">Back</span>

<p class="caption">Desifgn Concept Kestra Health PC 1</p>

</body>
</html>
```